Accounting firm needs a postcard design

We need a postcard design for our accounting office for a advertising campaign mailing we do yearly from a mail list we create. We are a full-service accounting office that has been in business for 35 years. I have attached our logo in different formats along with a document with a description of the services we provide. I have also attached my business card and the business card of our CPA. The business cards will have contact information for the postcard design. The contact email that will need to be on the postcard is contact@harlowledgerpartners.com.

```html
<!DOCTYPE html>
<html lang="en">
<head>
<meta charset="utf-8">
<title>Harlow Ledger Partners – Postcard</title>
<link rel="stylesheet" href="https://fonts.googleapis.com/css2?family=Lato:wght@300;400;700;900&display=swap">
<style>
  :root {
    --stage: #2b2b2b;
    --paper: #ffffff;
    --royal: #2c4fcb;
    --royal-deep: #1b2f8e;
    --navy: #1a2a78;
    --green: #4fb032;
    --green-bright: #63d13a;
    --sky: #1e8ed8;
    --ink: #1c2a5e;
  }
  * { box-sizing: border-box; margin: 0; padding: 0; }
  html, body { width: 1200px; height: 1177px; overflow: hidden; background: var(--stage); }
  body { position: relative; font-family: "Lato", Arial, sans-serif; }

  .postcard {
    position: absolute; left: 245px; width: 619px; height: 412px;
    background: var(--paper); overflow: hidden;
    transform: scale(1.2); transform-origin: 0 0;
  }
  .postcard--front { top: 76px; }
  .postcard--back { top: 606px; }
  .postcard > svg.shapes { position: absolute; inset: 0; width: 619px; height: 412px; }

  .headline {
    position: absolute; right: 266px; top: 28px; text-align: right;
    color: var(--paper); font-weight: 400; font-size: 18.5px; line-height: 20px; letter-spacing: .2px;
  }
  .headline__trust {
    position: absolute; left: 158px; top: 92px; width: 195px; text-align: center;
    color: var(--paper); font-weight: 900; font-size: 62px; line-height: 56px; letter-spacing: 1px;
    border-bottom: 5px solid var(--green-bright); padding-bottom: 2px;
  }
  .service-list { position: absolute; left: 200px; top: 169px; list-style: none; }
  .service-list li {
    color: var(--paper); font-size: 15px; line-height: 17.3px; padding-left: 11px; position: relative;
  }
  .service-list li::before {
    content: ""; position: absolute; left: 0; top: 4px;
    border-left: 6px solid var(--green-bright); border-top: 4.5px solid transparent; border-bottom: 4.5px solid transparent;
  }

  .brand { position: absolute; text-align: center; color: var(--ink); }
  .brand__mark { display: block; margin: 0 auto 5px; width: 34px; height: 34px; border-radius: 50%; background: var(--royal); }
  .brand__name { font-weight: 900; font-size: 13px; letter-spacing: 1px; color: var(--ink); white-space: nowrap; }
  .brand__tagline { font-size: 6.5px; color: var(--ink); white-space: nowrap; margin-top: 1px; }
  .postcard--front .brand { left: 30px; top: 310px; width: 230px; }
  .postcard--back .brand { left: 343px; top: 40px; width: 180px; }
  .postcard--back .brand__name { font-size: 10.5px; }
  .postcard--back .brand__tagline { font-size: 5.5px; }

  .contact { position: absolute; color: var(--paper); font-weight: 700; white-space: nowrap; }
  .postcard--front .contact--email { left: 60px; top: 384px; font-size: 16.5px; }
  .postcard--front .contact--phone { left: 440px; top: 367px; font-size: 21px; font-weight: 900; }
  .postcard--back .contact--email { left: 65px; top: 376px; font-size: 18px; }
  .postcard--back .contact--phone { left: 450px; top: 376px; font-size: 21px; font-weight: 900; }

  .stamp-box { position: absolute; left: 522px; top: 13px; width: 83px; height: 96px; border: 1px solid var(--navy); }

  .service-details { position: absolute; left: 18px; top: 61px; width: 370px; list-style: none; }
  .service-details li { position: relative; padding-left: 12px; margin-bottom: 9.5px; }
  .service-details li::before {
    content: ""; position: absolute; left: 0; top: 3px;
    border-left: 6px solid var(--paper); border-top: 4.5px solid transparent; border-bottom: 4.5px solid transparent;
  }
  .service-details h3 { color: var(--green-bright); font-weight: 700; font-size: 12.5px; line-height: 13px; }
  .service-details p { color: var(--paper); font-size: 9.6px; line-height: 11px; }
</style>
</head>
<body>

<section class="postcard postcard--front">
  <svg class="shapes" viewBox="0 0 619 412" aria-hidden="true">
    <defs>
      <linearGradient id="royal-sweep" x1="0" y1="0" x2="1" y2="0">
        <stop offset="0" stop-color="#3a66e0"/>
        <stop offset="1" stop-color="#1b2f8e"/>
      </linearGradient>
      <radialGradient id="plant-light" cx=".5" cy=".35" r=".7">
        <stop offset="0" stop-color="#f2fad0"/>
        <stop offset=".6" stop-color="#b8e07a"/>
        <stop offset="1" stop-color="#6fae3a"/>
      </radialGradient>
      <g id="hex-frame">
        <polygon points="0,-28 24.2,-14 24.2,14 0,28 -24.2,14 -24.2,-14" fill="#141414"/>
        <polygon points="0,-21 18.2,-10.5 18.2,10.5 0,21 -18.2,10.5 -18.2,-10.5" fill="#fff"/>
      </g>
    </defs>
    <path d="M40,0 H619 V255 C480,305 270,302 150,245 C110,225 88,180 72,120 Z" fill="url(#royal-sweep)"/>
    <path d="M176,248 C270,325 470,330 619,262 V280 C460,352 250,335 176,248 Z" fill="var(--green)"/>
    <circle cx="500" cy="125" r="126" fill="#fff"/>
    <circle cx="500" cy="125" r="120" fill="url(#plant-light)" role="img" aria-label="Photo: cupped hands holding coins with a young green plant sprouting"/>

    <polyline points="44,53 75,112 106,167 137,224" fill="none" stroke="var(--royal)" stroke-width="5"/>
    <use href="#hex-frame" x="44" y="53"/>
    <use href="#hex-frame" x="75" y="112"/>
    <use href="#hex-frame" x="106" y="167"/>
    <use href="#hex-frame" x="137" y="224"/>
    <g fill="none" stroke="var(--sky)" stroke-width="1.6">
      <rect x="35" y="42" width="18" height="22" rx="1.5"/>
      <line x1="39" y1="53" x2="49" y2="53"/><line x1="39" y1="57" x2="49" y2="57"/><line x1="39" y1="61" x2="46" y2="61"/>
    </g>
    <text x="44" y="49" text-anchor="middle" font-family="Lato, sans-serif" font-weight="900" font-size="6" fill="var(--sky)">TAX</text>
    <g fill="none" stroke="var(--sky)" stroke-width="1.6">
      <rect x="67" y="101" width="16" height="21" rx="1.5"/>
      <circle cx="72" cy="107" r="2.5"/>
      <line x1="70" y1="114" x2="80" y2="114"/><line x1="70" y1="118" x2="80" y2="118"/>
    </g>
    <g fill="var(--sky)">
      <rect x="101" y="167" width="3" height="7"/><rect x="106" y="164" width="3" height="10"/><rect x="111" y="161" width="3" height="13"/>
    </g>
    <circle cx="99" cy="163" r="4" fill="none" stroke="var(--sky)" stroke-width="1.4"/>
    <polyline points="101,160 108,156 112,158 117,153" fill="none" stroke="var(--sky)" stroke-width="1.6"/>
    <g fill="none" stroke="var(--sky)" stroke-width="1.6">
      <rect x="127" y="215" width="20" height="19" rx="1.5"/>
      <line x1="127" y1="220" x2="147" y2="220"/>
      <line x1="132" y1="212" x2="132" y2="217"/><line x1="142" y1="212" x2="142" y2="217"/>
    </g>
    <text x="137" y="232" text-anchor="middle" font-family="Lato, sans-serif" font-weight="900" font-size="10" fill="var(--sky)">$</text>

    <rect x="0" y="377" width="619" height="35" fill="var(--green)"/>
    <rect x="401" y="365" width="218" height="32" fill="var(--navy)" stroke="#cfd6ee" stroke-width="1"/>
    <circle cx="38" cy="394" r="12" fill="var(--navy)" stroke="#fff" stroke-width="2"/>
    <rect x="31" y="389" width="14" height="10" rx="1" fill="#fff"/>
    <polyline points="31,389 38,395 45,389" fill="none" stroke="var(--navy)" stroke-width="1.3"/>
    <circle cx="394" cy="381" r="14" fill="var(--sky)" stroke="#fff" stroke-width="2.5"/>
    <path d="M388,375 l3,-1 2,5 -2,1.5 c1,2.5 2.5,4 5,5 l1.5,-2 5,2 -1,3 c-6,1 -13,-6 -13.5,-13.5 z" fill="#fff"/>
  </svg>

  <h1 class="headline">INDIVIDUALIZED BUSINESS<br>&amp; PERSONAL ACCOUNTING<br>SERVICES YOU CAN</h1>
  <div class="headline__trust">TRUST</div>
  <ul class="service-list">
    <li>Tax Preparation</li>
    <li>Book Keeping</li>
    <li>Financial Reporting</li>
    <li>Payroll Processing</li>
  </ul>

  <div class="brand">
    <span class="brand__mark"></span>
    <div class="brand__name">HARLOW LEDGER PARTNERS</div>
    <div class="brand__tagline">Tax Preparation | Bookkeeping | Payroll | Entity Formation</div>
  </div>

  <div class="contact contact--email">contact@harlowledgerpartners.com</div>
  <div class="contact contact--phone">555-014-2270</div>
</section>

<section class="postcard postcard--back">
  <svg class="shapes" viewBox="0 0 619 412" aria-hidden="true">
    <defs>
      <linearGradient id="royal-sweep-back" x1="0" y1="0" x2="1" y2="1">
        <stop offset="0" stop-color="#3a66e0"/>
        <stop offset="1" stop-color="#1b2f8e"/>
      </linearGradient>
    </defs>
    <path d="M0,40 C60,28 140,26 196,34 C300,120 382,240 404,363 H0 Z" fill="url(#royal-sweep-back)"/>
    <path d="M200,33 C308,115 392,240 412,363" fill="none" stroke="var(--green)" stroke-width="7"/>
    <rect x="0" y="363" width="410" height="49" fill="var(--green)"/>
    <rect x="410" y="363" width="209" height="49" fill="var(--navy)"/>
    <circle cx="38" cy="388" r="13" fill="var(--navy)" stroke="#fff" stroke-width="2"/>
    <rect x="31" y="383" width="14" height="10" rx="1" fill="#fff"/>
    <polyline points="31,383 38,389 45,383" fill="none" stroke="var(--navy)" stroke-width="1.3"/>
    <circle cx="416" cy="388" r="15" fill="var(--sky)" stroke="#fff" stroke-width="2.5"/>
    <path d="M410,382 l3,-1 2,5 -2,1.5 c1,2.5 2.5,4 5,5 l1.5,-2 5,2 -1,3 c-6,1 -13,-6 -13.5,-13.5 z" fill="#fff"/>
  </svg>

  <div class="brand">
    <span class="brand__mark"></span>
    <div class="brand__name">HARLOW LEDGER PARTNERS</div>
    <div class="brand__tagline">Tax Preparation | Bookkeeping | Payroll | Entity Formation</div>
  </div>
  <div class="stamp-box"></div>

  <ul class="service-details">
    <li>
      <h3>TAX PREPARATION</h3>
      <p>With over 35 years of experience filing<br>tax returns, we are experts in tax preparation.<br>Including Personal Returns, Corporations, LLC's,<br>Partnerships and State Franchise Tax Returns.</p>
    </li>
    <li>
      <h3>BOOKKEEPING</h3>
      <p>Let us take over the day-to-day bookkeeping so you can get<br>back to running your business. We offer assistance with<br>ledger software setup and provide ongoing bookkeeping services.<br>Including frequent journal entries, accounts payables &amp; receivables,<br>sales tax reporting &amp; payments, account reconciliation, and more.</p>
    </li>
    <li>
      <h3>FINANCIAL REPORTING</h3>
      <p>We'll provide easy to understand financial reports that allow you and<br>your team to manage cash flow, create budgets and make forecasting<br>decisions. Depending on your needs, we can provide monthly, quarterly<br>or yearly financial statements.</p>
    </li>
    <li>
      <h3>PAYROLL PROCESSING</h3>
      <p>Whether you have 5 employees or 100+, payroll can be an overwhelming and<br>time consuming task. We offer full-service payroll processing. Including employee<br>onboarding, printed or direct deposit checks, quarterly payroll report filing, yearly<br>W-2/W-3 and 1099 printing and filing, and more</p>
    </li>
  </ul>

  <div class="contact contact--email">contact@harlowledgerpartners.com</div>
  <div class="contact contact--phone">555-014-2270</div>
</section>

</body>
</html>
```